Podcast Art for Tidy Belly Talks: Rising above Bramwell's Ache

Read carefully Please. Most submittals so far have not read this.

We're looking for stunning, eye-catching, innovative yet simple podcast art for our first Podcast

Background should be solid, one color

Tidy Belly Talks: Rising with Bramwell's Ache
with Marcus Lindqvar

Use our Brand Guide including logo, colors, and font
https://lnk.example-short.net/TBT2020StyleBook

Some Podcast Covers I like: https://casts.wavelotte.net/

Optional: Mighty Flusher graphic included above and/or my headshot uploaded below

As you can see humor / medutainment is part of the brand. As we are talking serious topic such as a disease many suffer from you can see the humor in the logo and "mighty flusher" . Here is the monologue for the first episode to give you a deeper feel on the content

https://files.papernook.net/doc/7qR_Lm3vTz9KpWx2eHdN4bYcA51FgUoJsMiXwQeVZ/view?share=1

Target Market(s)

Those who suffer from gut issues, are diagnosed with inflammatory bowel disease(IBD), Crohn's Disease or Ulcerative Colitis - also their coaches, doctors, practitioners so functional or integrative medicine doctors/coaches, gastroenterologists etc.

Industry/Entity Type

Health And Wellness

Font styles to use
Other font styles liked:
• Primary: Oswald bold. Secondary: Oswald Medium or light

Requirements
Must have
• 3000 x 3000 pixels
Simple and eye-catching
Brand Guide Logo
Brand Guide Font
Brand Guide Colors including accent color(s)
I did not select colors below because I have included our Brand guide. Please use the exact colors there.
Nice to have
• Maybe my headshot and/or the mighty flusher graphic - if not too busy and still looks good
Should not have
• - Look busy
- Reverse Logo
- Not follow the Brand Guide
- Anything in the background but one solid color from the brief

```html
<!DOCTYPE html>
<html lang="en">
<head>
<meta charset="utf-8">
<title>Tidy Belly Talks: Rising with Bramwell's Ache</title>
<link href="https://fonts.googleapis.com/css2?family=Oswald:wght@500;600;700&display=swap" rel="stylesheet">
<style>
  :root {
    --brand-pink: #db3a82;
    --brand-navy: #253f77;
    --brand-sky: #c5e6f0;
    --brand-yellow: #f4de7a;
  }
  html, body {
    margin: 0;
    padding: 0;
    width: 1200px;
    height: 1200px;
    overflow: hidden;
    background: var(--brand-navy);
  }
  .cover {
    position: relative;
    width: 1200px;
    height: 1200px;
    background: var(--brand-navy);
    font-family: "Oswald", "Arial Narrow", sans-serif;
    overflow: hidden;
  }
  .brand-panel {
    position: absolute;
    left: 0;
    top: 0;
    width: 434px;
    height: 1200px;
    background: var(--brand-pink);
    display: flex;
    align-items: center;
    justify-content: center;
  }
  .brand-divider {
    position: absolute;
    left: 434px;
    top: 0;
    width: 7px;
    height: 1200px;
    background: var(--brand-yellow);
  }
  .brand-name {
    margin: 0;
    color: var(--brand-sky);
    font-weight: 700;
    font-size: 104px;
    line-height: 0.98;
    text-align: center;
    text-transform: uppercase;
  }
  .show-title {
    position: absolute;
    left: 498px;
    top: 92px;
    margin: 0;
    color: var(--brand-sky);
    font-weight: 700;
    text-transform: uppercase;
  }
  .show-title span {
    display: block;
    line-height: 0.95;
  }
  .title-lead { font-size: 196px; letter-spacing: 1px; }
  .title-joiner {
    font-size: 92px;
    font-weight: 600;
    text-transform: none;
    margin: 6px 0 10px 10px;
  }
  .title-subject { font-size: 120px; }
  .title-close { font-size: 196px; }
  .host {
    position: absolute;
    left: 510px;
    top: 918px;
    color: var(--brand-yellow);
    text-transform: uppercase;
    font-weight: 500;
  }
  .host-label { display: block; font-size: 34px; line-height: 1; letter-spacing: 1px; }
  .host-first { display: block; font-size: 70px; line-height: 1.05; letter-spacing: 3px; }
  .host-last { display: block; font-size: 50px; line-height: 1; letter-spacing: 2px; }
  .host-photo {
    position: absolute;
    left: 846px;
    top: 786px;
    width: 282px;
    height: 282px;
    border: 7px solid var(--brand-pink);
    background: linear-gradient(160deg, #9a8e7c 0%, #c9bca8 45%, #f1eee9 100%);
  }
</style>
</head>
<body>
  <main class="cover">
    <section class="brand-panel">
      <p class="brand-name">Tidy<br>Belly<br>Talks</p>
    </section>
    <div class="brand-divider"></div>

    <h1 class="show-title">
      <span class="title-lead">Rising</span>
      <span class="title-joiner">With</span>
      <span class="title-subject">Bramwell's</span>
      <span class="title-close">Ache</span>
    </h1>

    <p class="host">
      <span class="host-label">With</span>
      <span class="host-first">Marcus</span>
      <span class="host-last">Lindqvar</span>
    </p>

    <div class="host-photo" role="img" aria-label="Headshot of host Marcus Lindqvar smiling, in a white shirt, against a stone wall"></div>
  </main>
</body>
</html>
```